Construction Company Website Design

I need a Website Design for a Construction Company. I have attached logo and business card design files (a.i) to match styles and text for the website. I will need design for 3 pages:
1. A Home page
2. A secondary page (will be different information pages)
3. A contact page with submision form
Website to look professional and match the 'theme' across all pages, using main colours / reverse colours as per design files. Must be clear it is a construction related website without being over the top. Happy for the construction related details (whether that be images/outlines/backgrounds etc to be fairly subtle and not overbearing on the contect of the pages. It will be the content that will be most important, not the images within.

Content has not yet been fully completed but attached is a site map. Each page will need a space for the insertion of the relevant heading and associated content for that particular page. Example can be used as per attached map. If it is preferable to have content completed for this to be a more succesful project please advise and I will complete and submit.

Target Market(s)

Clients for potential construction projects. These could be a range of people. All would be very professional, well educated and put a substantial expection on the quality of website provided.

Industry/Entity Type

Construction

Number of Pages Required

3 page

Font styles to use
Serif
Sans Serif
Other font styles liked:
• fonts preferable as per design files provided unless designer beleives a different font would suit better

Requirements
Must have
• Colour scheme to match logo and business card files provided. Fonts that match as per provided files. Pages must be consistent with the theme carrying across all pages. All pages must have contact details at the bottom of the page.
• Contents of page 1 - 'Home page': multiple tab options / logo link
• Contents of page 2 - 'Secondary page': Top and side navigation / area for information and/or images.
• Contents of page - 'Contact us page': Top and side navigation / Submission form / area for logos such as linkdin, facebook etc.
Nice to have
• Would be good to have a or some generic construction related images - outlines / shadows / effects etc. These might be background images or outlines related to the relevant industry and are consistent across the pages. Could be outlines of buildings, images of men with hardhats etc etc. Good to see colour scheme as per design files used
Should not have
• No pictures of houses. Generally no photos. If any imagery of people must not show faces/details.

```html
<!DOCTYPE html>
<html lang="en">
<head>
<meta charset="utf-8">
<title>KRA Constructions</title>
<link rel="stylesheet" href="https://fonts.googleapis.com/css2?family=Montserrat:wght@400;500;600;700;800&display=swap">
<style>
:root{
  --blue:#0e96d8;
  --blue-bright:#13a6ee;
  --navy:#07142a;
  --ink:#222222;
  --text:#333333;
  --grey-band:#e1e1e1;
  --footer:#151515;
  --white:#ffffff;
}
*{box-sizing:border-box;margin:0;padding:0}
html,body{width:1200px;height:2327px;overflow:hidden}
body{position:relative;font-family:"Montserrat",Arial,sans-serif;color:var(--text);background:var(--white)}
.abs{position:absolute}

/* Hero */
.hero{left:0;top:0;width:1200px;height:541px;background:linear-gradient(180deg,#0a1a33 0%,#0b2747 45%,#0a2039 75%,#101e30 100%)}
.hero::after{content:"";position:absolute;inset:0;background:radial-gradient(ellipse at 50% 60%,rgba(80,140,200,.25),rgba(0,0,0,0) 60%)}
.brand{left:46px;top:27px;color:var(--white);font-size:20px;font-weight:600;letter-spacing:1px;z-index:2}
.main-nav{right:46px;top:28px;display:flex;gap:12px;font-size:17px;font-weight:500;color:var(--white);z-index:2}
.main-nav .current{font-weight:700}
.main-nav .active{color:var(--blue-bright);font-weight:700}
.dropdown{left:754px;top:59px;width:191px;background:var(--white);padding:4px 10px;z-index:3;box-shadow:0 3px 8px rgba(0,0,0,.3)}
.dropdown li{list-style:none;font-size:14px;color:#444;padding:9px 2px 8px;border-bottom:1px solid #cfcfcf}
.dropdown li:last-child{border-bottom:none}
.cursor{z-index:4}
.hero-title{left:0;width:1200px;top:250px;text-align:center;color:var(--white);font-size:48px;font-weight:700;z-index:2}
.hero-title span{color:var(--blue-bright);font-weight:800;letter-spacing:1px}
.btn{top:325px;height:37px;font-size:15px;font-weight:700;letter-spacing:.5px;display:flex;align-items:center;justify-content:center;border-radius:3px;z-index:2}
.btn-solid{left:395px;width:194px;background:var(--blue);color:var(--white)}
.btn-outline{left:609px;width:195px;border:3px solid var(--blue);color:var(--blue)}
.scroll-cue{left:584px;top:498px;z-index:2}

/* Section headings */
.section-title{left:0;width:1200px;text-align:center;font-size:28px;font-weight:700;color:var(--ink)}
.section-title span{color:var(--blue)}
.title-rule{left:572px;width:56px;height:4px;background:var(--blue)}

/* About */
.about-copy{left:350px;width:500px;top:632px;text-align:center;font-size:19px;line-height:27px;color:var(--ink)}

/* Services */
.services{left:0;top:774px;width:1200px;height:566px;background:var(--grey-band)}
.service-card{width:349px;height:200px;border:2px solid var(--blue);box-shadow:4px 8px 12px rgba(0,0,0,.45);display:flex;flex-direction:column;align-items:center;justify-content:center;text-align:center;color:var(--white)}
.service-card h3{font-size:25px;font-weight:800;letter-spacing:.5px;line-height:25px;text-shadow:0 1px 3px rgba(0,0,0,.5)}
.service-card p{font-size:17px;line-height:21px;margin-top:10px;padding:0 24px}
.card-commercial{left:46px;top:873px;background:linear-gradient(160deg,#8a95a6,#4b4d58 55%,#2c2b32)}
.card-residential{left:426px;top:873px;background:linear-gradient(160deg,#1fb0f0,#0a8fd2)}
.card-residential h3{text-shadow:none}
.card-building{left:806px;top:873px;background:linear-gradient(170deg,#4d7fc0,#6f9bd0 45%,#3d5f86)}
.card-maintenance{left:239px;top:1101px;background:linear-gradient(160deg,#d9d4cc,#b7afa2 50%,#6e6a66)}
.card-management{left:613px;top:1101px;background:linear-gradient(160deg,#b9b4aa,#d6cfc0 50%,#8f8a80)}

/* News */
.news-kicker{left:46px;top:1373px;font-size:21px;color:var(--ink)}
.news-title{left:46px;top:1398px;font-size:26px;font-weight:700;color:var(--ink)}
.news-rule{left:46px;top:1440px;width:112px;height:2px;background:var(--blue)}
.news-intro{left:46px;top:1458px;width:830px;font-size:19px;line-height:27px;color:var(--ink)}
.feature-image{left:46px;top:1534px;width:587px;height:512px;background:linear-gradient(180deg,#4f8dd6 0%,#8bb7e6 40%,#6d6a55 70%,#5b4530 100%)}
.feature-card{left:64px;top:1846px;width:551px;height:184px;background:var(--white);padding:22px 12px}
.meta{font-size:15px;font-weight:600;color:var(--ink)}
.feature-card h3{font-size:27px;font-weight:700;color:var(--ink);margin-top:10px}
.feature-card p{font-size:16px;line-height:27px;margin-top:14px;color:var(--ink)}
.thumb{left:659px;width:156px;height:156px}
.thumb-1{top:1534px;background:linear-gradient(180deg,#e2a13e,#a2662a 60%,#4a2e18)}
.thumb-2{top:1714px;background:linear-gradient(160deg,#e2c54a,#c9cfd6 45%,#9aa3ad)}
.thumb-3{top:1892px;background:linear-gradient(180deg,#7d7c78,#a39a6f 55%,#d9b92f)}
.news-item{left:828px;width:330px}
.news-item h3{font-size:27px;font-weight:700;color:var(--ink);margin-top:10px}
.news-item h3.hover{color:var(--blue)}
.news-item .rule{width:46px;height:4px;background:var(--blue);margin-top:8px}
.news-item p{font-size:16px;line-height:27px;margin-top:10px;color:var(--ink)}
.news-item p.excerpt{width:250px}

/* Footer */
.site-footer{left:0;top:2085px;width:1200px;height:242px;background:var(--footer);color:var(--white)}
.foot-kicker{font-size:15px;font-weight:600}
.foot-title{font-size:18px;font-weight:700;margin-top:6px}
.foot-rule{width:72px;height:3px;background:var(--blue);margin-top:12px}
.contact-list{list-style:none;margin-top:24px}
.contact-list li{display:flex;align-items:center;gap:16px;font-size:15px;font-weight:600;height:33px}
.social{display:flex;gap:15px;margin-top:24px}
.social span{width:37px;height:37px;border-radius:50%;background:var(--blue);display:block}
</style>
</head>
<body>

<header class="abs hero" role="img" aria-label="Dark blue wireframe outline of city towers behind the headline"></header>
<div class="abs brand">KRA Constructions</div>
<nav class="abs main-nav">
  <span class="current">Home</span><span>About Us</span><span class="active">Services</span><span>Projects</span><span>Culture</span><span>News</span><span>Contact</span>
</nav>
<ul class="abs dropdown">
  <li>Commercial</li><li>Residential</li><li>Building</li><li>Maintenance</li><li>Project Management</li>
</ul>
<svg class="abs cursor" style="left:834px;top:44px" width="18" height="26" viewBox="0 0 18 26"><path d="M1 1 L1 20 L6 15 L9 23 L12 22 L9 14 L16 14 Z" fill="#fff" stroke="#000" stroke-width="1.3"/></svg>
<h1 class="abs hero-title">We build things <span>DIFFERENTLY</span></h1>
<a class="abs btn btn-solid">VIEW OUR PROJECTS</a>
<a class="abs btn btn-outline">CONTACT US</a>
<svg class="abs scroll-cue" width="32" height="22" viewBox="0 0 32 22"><path d="M4 4 L16 16 L28 4" fill="none" stroke="#fff" stroke-width="6" stroke-linecap="round" stroke-linejoin="round"/></svg>

<section>
  <h2 class="abs section-title" style="top:570px">About <span>Us</span></h2>
  <div class="abs title-rule" style="top:611px"></div>
  <p class="abs about-copy">Lorem ipsum dolor sit amet, consectetur adipiscing elit. Sed tincidunt nibh non vulputate congue. Sed sit amet tempus elit. Donec sodales eros sagittis mattis tempor.</p>
</section>

<section class="abs services"></section>
<h2 class="abs section-title" style="top:803px">What We <span>Do</span></h2>
<div class="abs title-rule" style="top:844px;left:553px;width:94px;height:3px"></div>
<div class="abs service-card card-commercial" role="img" aria-label="Commercial building under construction with scaffolding"><h3>COMMERCIAL</h3></div>
<div class="abs service-card card-residential" role="img" aria-label="Residential service highlighted in blue"><h3>RESIDENTIAL</h3><p>Lorem ipsum dolor sit amet, consectetur adipiscing elit. Sed tincidunt nibh non vulputate congue.</p></div>
<svg class="abs cursor" style="left:616px;top:940px" width="18" height="26" viewBox="0 0 18 26"><path d="M1 1 L1 20 L6 15 L9 23 L12 22 L9 14 L16 14 Z" fill="#fff" stroke="#000" stroke-width="1.3"/></svg>
<div class="abs service-card card-building" role="img" aria-label="Tall glass towers with tower cranes against the sky"><h3>BUILDING</h3></div>
<div class="abs service-card card-maintenance" role="img" aria-label="Worker with hard hat and tool belt in a bright room"><h3>MAINTENANCE</h3></div>
<div class="abs service-card card-management" role="img" aria-label="Hard hats and building plans on a desk"><h3>PROJECT<br>MANAGEMENT</h3></div>

<section>
  <p class="abs news-kicker">From KRA Constructions</p>
  <h2 class="abs news-title">Latest News and Events</h2>
  <div class="abs news-rule"></div>
  <p class="abs news-intro">Lorem ipsum dolor sit amet, consectetur adipiscing elit. Sed tincidunt nibh non vulputate congue. Sed sit amet tempus elit.</p>
  <div class="abs feature-image" role="img" aria-label="Excavator digging earth under a blue sky"></div>
  <article class="abs feature-card">
    <p class="meta">January 01 / Residential Constructions</p>
    <h3>Lates News</h3>
    <p>Lorem ipsum dolor sit amet, consectetur adipiscing elit. Sed tincidunt nibh non vulputate congue. Sed sit amet tempus elit.</p>
  </article>

  <div class="abs thumb thumb-1" role="img" aria-label="Silhouetted builders on a site at sunset"></div>
  <article class="abs news-item" style="top:1543px">
    <p class="meta">February 11 / Building Constructions</p>
    <h3>News 1</h3><div class="rule"></div>
    <p class="excerpt">Lorem ipsum dolor sit amet, consectetur adipiscing elit...</p>
  </article>

  <div class="abs thumb thumb-2" role="img" aria-label="Rolled plans, hard hat and measuring tape"></div>
  <article class="abs news-item" style="top:1723px">
    <p class="meta">December 20 / Project Management</p>
    <h3 class="hover">News 2</h3><div class="rule"></div>
    <p class="excerpt">Lorem ipsum dolor sit amet, consectetur adipiscing elit...</p>
  </article>
  <svg class="abs cursor" style="left:920px;top:1774px" width="18" height="26" viewBox="0 0 18 26"><path d="M1 1 L1 20 L6 15 L9 23 L12 22 L9 14 L16 14 Z" fill="#fff" stroke="#000" stroke-width="1.3"/></svg>

  <div class="abs thumb thumb-3" role="img" aria-label="Hand over a yellow model of buildings and a crane"></div>
  <article class="abs news-item" style="top:1901px">
    <p class="meta">March 07 / Maintenance</p>
    <h3>News 3</h3><div class="rule"></div>
    <p class="excerpt">Lorem ipsum dolor sit amet, consectetur adipiscing elit...</p>
  </article>
</section>

<footer class="abs site-footer">
  <div class="abs" style="left:46px;top:36px">
    <p class="foot-kicker">AUSTRALIA</p>
    <p class="foot-title">Headquarters</p>
    <div class="foot-rule"></div>
    <ul class="contact-list">
      <li><svg width="18" height="18" viewBox="0 0 24 24"><path d="M6.6 10.8a15 15 0 0 0 6.6 6.6l2.2-2.2a1 1 0 0 1 1-.25 11.4 11.4 0 0 0 3.6.57 1 1 0 0 1 1 1V20a1 1 0 0 1-1 1A17 17 0 0 1 3 4a1 1 0 0 1 1-1h3.5a1 1 0 0 1 1 1c0 1.25.2 2.450.57 3.57a1 1 0 0 1-.25 1z" fill="#fff"/></svg>0400 123 987</li>
      <li><svg width="18" height="14" viewBox="0 0 18 14"><rect x="0.5" y="0.5" width="17" height="13" fill="#fff"/><path d="M1 1 L9 8 L17 1 M1 13 L7 7 M17 13 L11 7" fill="none" stroke="#151515" stroke-width="1.4"/></svg>hello@kraconstructions.example</li>
      <li><svg width="16" height="20" viewBox="0 0 16 20"><path d="M8 0a8 8 0 0 0-8 8c0 6 8 12 8 12s8-6 8-12a8 8 0 0 0-8-8z" fill="#fff"/><circle cx="8" cy="8" r="3" fill="#151515"/></svg>14 Harbour Lane, Eastbrook 2100</li>
    </ul>
  </div>
  <div class="abs" style="left:809px;top:36px">
    <p class="foot-kicker">GET IN TOUCH</p>
    <p class="foot-title">Follow Our Activity</p>
    <div class="foot-rule"></div>
    <div class="social"><span></span><span></span><span></span><span></span></div>
  </div>
</footer>

</body>
</html>
```